Terra Swift Business Card Design

We need to improve the design of our current business card. We are a erosion control, hydro seeding company that serves many markets. We are attaching the current business card and our logo as reference. You may also visit our site at www.terraswiftllc.example to reference.

```html
<!DOCTYPE html>
<html lang="en">
<head>
<meta charset="utf-8">
<title>Terra Swift Business Card</title>
<link href="https://fonts.googleapis.com/css2?family=Lato:wght@400;700;900&display=swap" rel="stylesheet">
<style>
  :root {
    --bg-dark: #1a1a1a;
    --bg-mid: #3a3a3a;
    --card-black: #1c1c1c;
    --card-white: #ffffff;
    --green-deep: #006a3c;
    --green-bright: #2fa650;
    --green-text: #0f7a3e;
    --ink: #2b2b2b;
    --ink-soft: #5a5a5a;
    --list-text: #e8e8e8;
  }
  * { margin: 0; padding: 0; box-sizing: border-box; }
  html, body { width: 1200px; height: 875px; overflow: hidden; }
  body {
    background: linear-gradient(135deg, var(--bg-mid) 0%, var(--bg-dark) 70%);
    font-family: 'Lato', sans-serif;
    position: relative;
  }
  .card {
    position: absolute;
    width: 560px;
    height: 320px;
    border-radius: 18px;
    overflow: hidden;
    box-shadow: 0 18px 40px rgba(0,0,0,0.55);
  }

  /* Back card */
  .card-back { left: 60px; top: 100px; background: var(--card-black); }
  .card-back .brand {
    position: absolute; left: 36px; top: 40px;
    font-weight: 900; font-size: 46px; color: var(--green-bright);
    letter-spacing: -0.5px;
  }
  .card-back .accent {
    position: absolute; right: 0; top: 0; width: 180px; height: 150px;
  }
  .services {
    position: absolute; list-style: none;
    color: var(--list-text); font-size: 14px; line-height: 19px;
  }
  .services li { display: flex; align-items: center; gap: 9px; }
  .services li::before {
    content: ""; width: 8px; height: 8px; border-radius: 50%;
    background: var(--green-bright); flex: none;
  }
  .services-left { left: 36px; top: 124px; }
  .services-right { left: 300px; top: 124px; }

  /* Front card */
  .card-front { left: 580px; top: 455px; background: var(--card-white); }
  .card-front .panel { position: absolute; right: 0; top: 0; width: 240px; height: 320px; }
  .card-front .panel-brand {
    position: absolute; right: 34px; top: 148px;
    font-weight: 900; font-size: 28px; color: var(--card-white);
  }
  .person { position: absolute; left: 34px; top: 44px; }
  .person .name {
    font-weight: 900; font-size: 30px; color: var(--green-deep);
    letter-spacing: 0.3px; line-height: 1;
  }
  .person .role {
    font-size: 15px; color: var(--green-bright); margin-top: 4px;
  }
  .person .rule {
    width: 56px; height: 3px; background: var(--green-deep); margin-top: 10px;
  }
  .contact { position: absolute; left: 34px; top: 132px; color: var(--ink-soft); font-size: 13.5px; }
  .contact .row { display: flex; gap: 10px; align-items: flex-start; line-height: 18px; }
  .contact svg { width: 12px; height: 12px; margin-top: 3px; fill: var(--green-bright); flex: none; }
  .address strong { color: var(--ink); font-weight: 700; display: block; }
  .lines { margin-top: 10px; }
</style>
</head>
<body>

<section class="card card-back" aria-label="Business card back">
  <svg class="accent" viewBox="0 0 180 150" aria-hidden="true">
    <path d="M40 0 H180 V150 C120 150 60 90 40 0 Z" fill="#2b2b2b"/>
  </svg>
  <div class="brand">Terra Swift</div>
  <ul class="services services-left">
    <li>Erosion Control Installation</li>
    <li>Seed and Straw</li>
    <li>Hydroseeding</li>
    <li>Compost Blankets</li>
    <li>Drill Seeding</li>
    <li>Erosion Control Blankets</li>
    <li>Turf Reinforcement Matting</li>
    <li>Custom Soil Amending</li>
    <li>Native, Pollinator, &amp; Wetland Seeding</li>
  </ul>
  <ul class="services services-right">
    <li>Silt Fence</li>
    <li>Filter Sock</li>
    <li>Construction Entrances</li>
    <li>Clearing &amp; Grubbing</li>
    <li>Skimmer Basins</li>
    <li>Diversion Ditches</li>
    <li>Site Prep &amp; Grading</li>
    <li>Gravel Access Roads</li>
    <li>Laydown Construction &amp; Restoration</li>
  </ul>
</section>

<section class="card card-front" aria-label="Business card front">
  <svg class="panel" viewBox="0 0 240 320" aria-hidden="true">
    <path d="M70 0 H240 V320 H60 C10 240 10 80 70 0 Z" fill="var(--green-deep)"/>
    <path d="M200 0 H240 V320 H170 C230 220 230 100 200 0 Z" fill="var(--green-bright)" opacity="0.55"/>
  </svg>
  <div class="panel-brand">Terra Swift</div>

  <div class="person">
    <div class="name">DANA WHITFIELD</div>
    <div class="role">Chief Operating Officer</div>
    <div class="rule"></div>
  </div>

  <div class="contact">
    <div class="row address">
      <svg viewBox="0 0 12 12"><path d="M6 0a4 4 0 0 0-4 4c0 3 4 8 4 8s4-5 4-8a4 4 0 0 0-4-4zm0 5.6A1.6 1.6 0 1 1 6 2.4a1.6 1.6 0 0 1 0 3.2z"/></svg>
      <div>
        <strong>Corporate Headquarters</strong>
        <strong>Terra Swift, LLC</strong>
        27 Alder Creek Road<br>Riverbend, NC 28000
      </div>
    </div>
    <div class="lines">
      <div class="row"><svg viewBox="0 0 12 12"><path d="M2.4 0.5l2 2-1.1 1.6a7 7 0 0 0 4.6 4.6L9.5 7.6l2 2-1.4 1.9C5 11.5 0.5 7 0.5 1.9z"/></svg>(555) 010-1686</div>
      <div class="row"><svg viewBox="0 0 12 12"><rect x="3" y="0" width="6" height="12" rx="1.2"/></svg>(555) 010-1685</div>
      <div class="row"><svg viewBox="0 0 12 12"><rect x="1" y="4" width="10" height="6" rx="1"/><rect x="3" y="0.5" width="6" height="3"/></svg>(555) 010-0310</div>
      <div class="row"><svg viewBox="0 0 12 12"><path d="M0 2h12v8H0zM0 2l6 4.5L12 2" /></svg>info@terraswiftllc.example</div>
      <div class="row"><svg viewBox="0 0 12 12"><circle cx="6" cy="6" r="6"/></svg>www.terraswiftllc.example</div>
    </div>
  </div>
</section>

</body>
</html>
```